Creative Design "Size Chart" for a Clothing Product

Hi, My dear friends! I am looking to do a contest to design a unique creative "Size Chart" for our clothing line. See Attached the Sizes & Ideas Thanks Good Luck Dolph

Colors

Designer to choose colors to be used in the design.

```html
<!DOCTYPE html>
<html lang="en">
<head>
<meta charset="utf-8">
<title>Size Chart</title>
<link href="https://fonts.googleapis.com/css2?family=Roboto:wght@400;500;700&family=Roboto+Condensed:wght@400;500&display=swap" rel="stylesheet">
<style>
  :root {
    --mens: #3a9fc0;
    --womens: #e9609f;
    --boys: #3bb44a;
    --girls: #f7941e;
    --ink: #444444;
    --row-alt: #e6e6e6;
    --rule: #bdbdbd;
    --paper: #ffffff;
  }
  * { margin: 0; padding: 0; box-sizing: border-box; }
  html, body { width: 1200px; height: 1200px; overflow: hidden; background: var(--paper); }
  body { position: relative; font-family: "Roboto", sans-serif; color: var(--ink); }

  .chart {
    position: absolute;
    width: 461px;
    height: 551px;
    border: 4px solid var(--accent);
    background: var(--paper);
  }
  .chart--mens   { --accent: var(--mens);   --tint: #e4f2f7; left: 123px; top: 34px; }
  .chart--womens { --accent: var(--womens); --tint: #fbe6f0; left: 618px; top: 34px; }
  .chart--boys   { --accent: var(--boys);   --tint: #e5f5e7; left: 123px; top: 618px; }
  .chart--girls  { --accent: var(--girls);  --tint: #fef0df; left: 618px; top: 618px; }

  .chart__title {
    margin-top: 23px;
    text-align: center;
    font-weight: 700;
    font-size: 42px;
    line-height: 46px;
    color: var(--accent);
  }
  .chart__unit {
    text-align: center;
    font-size: 14px;
    font-weight: 500;
    color: var(--ink);
    margin-top: 4px;
    line-height: 18px;
  }

  .size-table {
    position: absolute;
    left: 0; top: 97px;
    width: 100%;
    border-collapse: collapse;
    table-layout: fixed;
  }
  .size-table th, .size-table td {
    text-align: center;
    font-family: "Roboto Condensed", sans-serif;
  }
  .size-table thead th {
    background: var(--accent);
    color: var(--paper);
    height: 25px;
    font-size: 14px;
    font-weight: 500;
    border-left: 1px solid rgba(255,255,255,0.7);
  }
  .size-table thead th:first-child { border-left: none; }
  .size-table tbody td {
    height: 42px;
    font-size: 16px;
    color: #333;
    border-left: 1px solid var(--rule);
  }
  .size-table tbody th {
    font-family: "Roboto", sans-serif;
    font-weight: 400;
    font-size: 17px;
    color: var(--ink);
    text-align: left;
    padding-left: 30px;
    height: 42px;
  }
  .size-table tbody tr:nth-child(2) { background: var(--row-alt); }
  .size-table .label-col { width: 113px; }
  .chart--girls .size-table .label-col { width: 112px; }
  .chart--womens .size-table thead th { font-size: 13px; letter-spacing: -0.3px; }
  .chart--womens .size-table tbody td { font-size: 15px; }

  .chart__notes {
    position: absolute;
    left: 22px; top: 224px;
    list-style: none;
    font-size: 14px;
    line-height: 19.5px;
    color: var(--accent);
  }
  .chart__notes li { position: relative; padding-left: 17px; }
  .chart__notes li::before {
    content: "";
    position: absolute;
    left: 0; top: 5px;
    width: 9px; height: 9px;
    border-radius: 50%;
    background: var(--accent);
  }

  .chart__garment {
    position: absolute;
    left: 125px; top: 280px;
    width: 207px; height: 244px;
    border-radius: 30px 30px 10px 10px;
    background: linear-gradient(180deg, var(--tint), #ffffff);
  }
</style>
</head>
<body>

<section class="chart chart--mens">
  <h2 class="chart__title">MENS</h2>
  <p class="chart__unit">(IN INCHES)</p>
  <table class="size-table">
    <colgroup><col class="label-col"><col><col><col><col><col><col></colgroup>
    <thead><tr><th></th><th>XXS</th><th>XS</th><th>S</th><th>M</th><th>L</th><th>XL</th></tr></thead>
    <tbody>
      <tr><th>Chest</th><td>34-36</td><td>36-38</td><td>38-40</td><td>40-42</td><td>43-45</td><td>45-48</td></tr>
      <tr><th>Waist</th><td>28-30</td><td>30-32</td><td>32-34</td><td>34-36</td><td>36-40</td><td>40-44</td></tr>
    </tbody>
  </table>
  <ul class="chart__notes">
    <li>All measurements shown will have a tolerance of 0.5 inches</li>
    <li>All measurements shown are of the garment.</li>
  </ul>
  <div class="chart__garment" role="img" aria-label="Men's polo shirt outline with dashed chest and waist measurement lines"></div>
</section>

<section class="chart chart--womens">
  <h2 class="chart__title">WOMENS</h2>
  <p class="chart__unit">(IN INCHES)</p>
  <table class="size-table">
    <colgroup><col class="label-col"><col><col><col><col><col><col><col></colgroup>
    <thead><tr><th></th><th>XS (0-2)</th><th>S (4-6)</th><th>M (8-10)</th><th>L (12-14)</th><th>XL (14-16)</th><th>2X (18)</th><th>3X (20)</th></tr></thead>
    <tbody>
      <tr><th>Chest</th><td>32-34</td><td>34-36</td><td>36-38</td><td>38-40</td><td>40-42</td><td>42-44</td><td>44-46</td></tr>
      <tr><th>Waist</th><td>26-28</td><td>28-30</td><td>30-32</td><td>32-34</td><td>34-36</td><td>36-38</td><td>38-40</td></tr>
    </tbody>
  </table>
  <ul class="chart__notes">
    <li>All measurements shown will have a tolerance of 0.5 inches</li>
    <li>All measurements shown are of the garment.</li>
  </ul>
  <div class="chart__garment" role="img" aria-label="Women's fitted polo shirt outline with dashed chest and waist measurement lines"></div>
</section>

<section class="chart chart--boys">
  <h2 class="chart__title">BOYS</h2>
  <p class="chart__unit">(IN INCHES)</p>
  <table class="size-table">
    <colgroup><col class="label-col"><col><col><col><col><col><col></colgroup>
    <thead><tr><th></th><th>XXS</th><th>XS</th><th>S</th><th>M</th><th>L</th><th>XL</th></tr></thead>
    <tbody>
      <tr><th>Chest</th><td>20-23</td><td>23-26</td><td>26-29</td><td>29-32</td><td>32-35</td><td>35-38</td></tr>
      <tr><th>Waist</th><td>19-21</td><td>21-23</td><td>22-25</td><td>25-27</td><td>27-29</td><td>29-31</td></tr>
    </tbody>
  </table>
  <ul class="chart__notes">
    <li>All measurements shown will have a tolerance of 0.5 inches</li>
    <li>All measurements shown are of the garment.</li>
  </ul>
  <div class="chart__garment" role="img" aria-label="Boys' polo shirt outline with dashed chest and waist measurement lines"></div>
</section>

<section class="chart chart--girls">
  <h2 class="chart__title">GIRLS</h2>
  <p class="chart__unit">(IN INCHES)</p>
  <table class="size-table">
    <colgroup><col class="label-col"><col><col><col><col><col><col></colgroup>
    <thead><tr><th></th><th>XXS</th><th>XS</th><th>S</th><th>M</th><th>L</th><th>XL</th></tr></thead>
    <tbody>
      <tr><th>Chest</th><td>19-22</td><td>22-25</td><td>25-28</td><td>28-31</td><td>31-34</td><td>34-37</td></tr>
      <tr><th>Waist</th><td>18-20</td><td>20-22</td><td>22-24</td><td>24-26</td><td>26-28</td><td>28-30</td></tr>
    </tbody>
  </table>
  <ul class="chart__notes">
    <li>All measurements shown will have a tolerance of 0.5 inches</li>
    <li>All measurements shown are of the garment.</li>
  </ul>
  <div class="chart__garment" role="img" aria-label="Girls' fitted polo shirt outline with dashed chest and waist measurement lines"></div>
</section>

</body>
</html>
```